Business Card needed for AI Technology Company

About the Business:

Lorvane Crest Industries is a high-tech firm specializing in advanced AI systems, industrial mathematics, and intelligent decision architectures. We design and build AI agents, mathematical models, and algorithmic systems for the financial sector, mining, and supply chains. Our solutions are engineered to improve decision speed, accuracy, and resilience—especially in uncertain, high-impact environments.

The name "Lorvane Crest" comes from a concept in complex systems and economics referring to rare, powerful outlier events that exceed conventional expectations—just like the transformative outcomes we engineer for our clients.

Can use either logo with blue or white background. Inline is preferred. (See attached). Use logo colours where possible.

Front - Initial Thoughts (Can vary)
- logo
- lorvanecrestindustries.com
- tagline We Deliver Lorvane Crest Outcomes—Transformative AI Solutions Beyond Expectations.

Back Left ( Details) - Initial Thoughts (Can vary)
- <Name>
- Founder & Director
- phone: <number>
- email: <email>
- <address>

Back Right - Initial Thoughts (Can vary)
- Curious what AI can do for you? Scan to unlock the answer. (Call To Action)
- QR Code with logo embedded - dynamic link - I can repalce this

Services (Optional - but may be crowded)
• AI Agents & Components
• Advanced Software Engineering
• Decision Modelling & Analytics

Happy for variations to the above

Target Market(s)

Primary (Ordered 1 is priority) 1 Financial Sector (Risk manager, trading firms, investment managers) 2 Mining (Operations); 3 Supply Change Management(Logistic Managers, Procurement teams); 4 Energy and Utility(Renewables and Grid operators) Geography Australia, Canada, UK and USA

Contact Information for Business Card

Use the attached logos

Requirements
Must have
• Attached logo

```html
<!DOCTYPE html>
<html lang="en">
<head>
<meta charset="UTF-8">
<title>Lorvane Crest Industries — Business Card</title>
<link href="https://fonts.googleapis.com/css2?family=Poppins:wght@400;500;600;700&display=swap" rel="stylesheet">
<style>
  :root {
    --navy: #1b3566;
    --navy-deep: #102650;
    --orange: #d5501c;
    --orange-light: #e8743a;
    --card-bg: #f4f6f9;
    --card-glow: #ffffff;
    --stage: #e7e3dd;
    --muted-light: #d9dee8;
  }
  * { box-sizing: border-box; margin: 0; padding: 0; }
  html, body {
    width: 1200px;
    height: 970px;
    overflow: hidden;
    background: var(--stage);
    font-family: "Poppins", sans-serif;
  }
  .business-card {
    position: absolute;
    left: 50px;
    top: 172px;
    width: 1100px;
    height: 626px;
    border-radius: 26px;
    overflow: hidden;
    background: radial-gradient(ellipse at 35% 30%, var(--card-glow) 0%, var(--card-bg) 60%, #e8ecf2 100%);
    box-shadow: 0 18px 40px rgba(0,0,0,0.18);
  }
  .card-waves {
    position: absolute;
    inset: 0;
  }
  .brand-mark {
    position: absolute;
    left: 238px;
    top: 110px;
    width: 120px;
    height: 120px;
    border-radius: 50%;
    background: var(--navy);
  }
  .brand-name {
    position: absolute;
    left: 89px;
    top: 250px;
    width: 430px;
    text-align: center;
    color: var(--navy);
    font-weight: 600;
    font-size: 46px;
    line-height: 1.05;
    letter-spacing: 0.5px;
    text-transform: uppercase;
  }
  .brand-tagline {
    position: absolute;
    left: 89px;
    top: 352px;
    width: 430px;
    text-align: center;
    color: var(--navy);
    font-weight: 600;
    font-size: 17px;
    letter-spacing: 0.6px;
  }
  .person {
    position: absolute;
    right: 56px;
    top: 80px;
    text-align: right;
  }
  .person-name {
    color: var(--navy);
    font-weight: 700;
    font-size: 33px;
    letter-spacing: 0.3px;
    line-height: 1.2;
  }
  .person-title {
    color: var(--orange);
    font-weight: 400;
    font-size: 25px;
    line-height: 1.2;
  }
  .address {
    position: absolute;
    right: 56px;
    top: 428px;
    text-align: right;
    color: var(--muted-light);
    font-size: 25px;
    line-height: 34px;
    font-weight: 400;
  }
  .contact-list {
    position: absolute;
    right: 56px;
    top: 516px;
    list-style: none;
    text-align: right;
    color: var(--muted-light);
    font-size: 25px;
    line-height: 36px;
  }
  .contact-item {
    display: flex;
    justify-content: flex-end;
    align-items: center;
    gap: 12px;
  }
  .contact-icon {
    width: 28px;
    height: 28px;
    flex: none;
  }
  .social-row {
    position: absolute;
    left: 89px;
    top: 547px;
    display: flex;
    gap: 19px;
  }
  .social-dot {
    width: 40px;
    height: 40px;
    border-radius: 50%;
    background: var(--orange);
  }
</style>
</head>
<body>
  <div class="business-card">
    <svg class="card-waves" viewBox="0 0 1100 626" width="1100" height="626" aria-hidden="true">
      <defs>
        <linearGradient id="navyFill" x1="0" y1="0" x2="1" y2="1">
          <stop offset="0" stop-color="#244578"/>
          <stop offset="1" stop-color="#0f2350"/>
        </linearGradient>
        <linearGradient id="orangeFill" x1="0" y1="0" x2="1" y2="0">
          <stop offset="0" stop-color="#c9461a"/>
          <stop offset="0.3" stop-color="#e8743a"/>
          <stop offset="1" stop-color="#c1401a"/>
        </linearGradient>
      </defs>
      <path d="M0 361 C 120 460, 230 512, 360 506 C 600 496, 850 300, 1100 325 L 1100 626 L 0 626 Z" fill="url(#orangeFill)"/>
      <path d="M0 392 C 130 480, 230 534, 360 532 C 600 526, 850 340, 1100 360 L 1100 626 L 0 626 Z" fill="#f1dcd3"/>
      <path d="M0 400 C 130 488, 230 542, 360 540 C 600 534, 850 350, 1100 370 L 1100 626 L 0 626 Z" fill="url(#navyFill)"/>
    </svg>

    <div class="brand-mark"></div>
    <div class="brand-name">Lorvane Crest<br>Industries</div>
    <div class="brand-tagline">Industrial AI &amp; Mathematical Intelligence</div>

    <div class="person">
      <div class="person-name">NOLAN R. ASHBY</div>
      <div class="person-title">Founder &amp; Director</div>
    </div>

    <div class="address">
      4820 W. Meridian Ave.<br>
      Suite 210, Arizona 85004
    </div>

    <ul class="contact-list">
      <li class="contact-item">
        <span>+1 480 -555-0172</span>
        <svg class="contact-icon" viewBox="0 0 28 28" aria-hidden="true">
          <circle cx="14" cy="14" r="14" fill="var(--orange)"/>
          <path d="M10 7 L12.5 7 L13.5 11 L11.8 12.3 C12.6 14.2 13.8 15.4 15.7 16.2 L17 14.5 L21 15.5 L21 18 C21 19.2 20 20 18.8 20 C13 19.6 8.4 15 8 9.2 C8 8 8.8 7 10 7 Z" fill="#fff"/>
        </svg>
      </li>
      <li class="contact-item">
        <span>hello@lorvanecrest.com</span>
        <svg class="contact-icon" viewBox="0 0 28 28" aria-hidden="true">
          <circle cx="14" cy="14" r="14" fill="var(--orange)"/>
          <rect x="7.5" y="9" width="13" height="10" rx="1.2" fill="none" stroke="#fff" stroke-width="1.8"/>
          <path d="M8 10 L14 14.8 L20 10" fill="none" stroke="#fff" stroke-width="1.8"/>
        </svg>
      </li>
    </ul>

    <div class="social-row">
      <span class="social-dot"></span>
      <span class="social-dot"></span>
      <span class="social-dot"></span>
    </div>
  </div>
</body>
</html>
```